VELTA CORE

I am in this industry for last 15 years we have done lots of commercial site like we work with BRAVEN costruction, lumo properties, TWD, penwick construction.
We do all domestic and commercial wall and floor tiling, swimming pools, spas, paving, marbles blue stones and muchmore.

Specializing in the wall and floor Tiling, Waterproofing and floor preparations

Industry/Entity Type

Industry

Number of Pages Required

1 page

Font styles to use
Serif
Decorative

Colors

Designer to choose colors to be used in the design.

Requirements
Must have
• domestic and commercial indoor tiling, bathroom tiling and paving pictures
Nice to have
• beautiful bathroom pictures with tile

```html
<!DOCTYPE html>
<html lang="en">
<head>
<meta charset="utf-8">
<title>VELTA CORE – Wall and Floor Tiling</title>
<link href="https://fonts.googleapis.com/css2?family=Poppins:wght@300;400;500;600&family=Roboto+Slab:wght@300;400&display=swap" rel="stylesheet">
<style>
:root{
  --ink:#1f2230;
  --muted:#7a7f8c;
  --faint:#b9bcc4;
  --accent:#2eaef0;
  --violet:#6c4bfb;
  --light:#f4f4f6;
  --footer:#3e4a5c;
  --footer-deep:#35404f;
  --white:#ffffff;
}
*{margin:0;padding:0;box-sizing:border-box}
html,body{width:1200px;height:3383px;overflow:hidden}
body{position:relative;background:var(--white);font-family:'Poppins',sans-serif;color:var(--ink)}
.abs{position:absolute}
.serif{font-family:'Roboto Slab',serif}

/* header */
.site-header{left:0;top:0;width:1200px;height:81px;background:var(--white);box-shadow:0 1px 6px rgba(0,0,0,.06)}
.brand{left:88px;top:26px;font-size:19px;font-weight:500;letter-spacing:.5px;color:#333}
.nav{right:88px;top:0;display:flex;gap:34px;height:81px;align-items:center;font-size:13px;color:#333}
.nav .active{color:var(--accent);position:relative}
.nav .active::before{content:"";position:absolute;left:0;right:0;top:-30px;height:2px;background:var(--accent)}

/* hero */
.hero{left:0;top:81px;width:1200px;height:591px;background:linear-gradient(135deg,#c9ccd0 0%,#e4e6e8 35%,#f2f2f2 55%,#b8bcc1 100%)}
.hero-shade{left:0;top:81px;width:1200px;height:591px;background:rgba(20,25,30,.28)}
.hero-kicker{left:0;width:1200px;top:316px;text-align:center;color:var(--white);font-size:22px;font-weight:300}
.hero-title{left:0;width:1200px;top:340px;text-align:center;color:var(--white);font-size:44px;font-weight:300}
.hero-btn{left:505px;top:410px;width:190px;height:45px;background:var(--white);color:#333;font-size:11px;font-weight:500;letter-spacing:.5px;display:flex;align-items:center;justify-content:center}
.hero-arrow{top:356px;width:44px;height:44px;border:2px solid rgba(255,255,255,.85);border-radius:50%}

/* partners */
.partner{top:740px;height:44px;display:flex;align-items:center;gap:10px;font-size:16px;font-weight:600;color:#6d7280;letter-spacing:.5px}
.partner i{display:block;width:26px;height:26px;border-radius:50%;background:#c8cbd2}

/* about */
.eyebrow{font-size:11px;letter-spacing:1px;color:var(--faint);text-transform:uppercase}
.about-heading{left:88px;top:932px;font-size:27px;line-height:37px;font-weight:400;color:var(--ink)}
.body-text{font-size:12.5px;line-height:26px;color:var(--muted)}
.btn-accent{background:var(--accent);color:var(--white);font-size:11px;font-weight:500;display:flex;align-items:center;justify-content:center}
.about-photo{left:600px;top:852px;width:600px;height:445px;background:linear-gradient(135deg,#d9d4cc 0%,#b9a27a 45%,#c9933e 70%,#8d7b62 100%);box-shadow:0 30px 40px -20px rgba(0,0,0,.25)}

/* services band */
.services{left:0;top:1389px;width:1200px;height:438px;background:var(--violet);color:var(--white)}
.services h2{position:absolute;left:0;width:1200px;top:100px;text-align:center;font-family:'Roboto Slab',serif;font-weight:400;font-size:27px}
.services p{position:absolute;left:330px;width:540px;top:146px;text-align:center;font-size:12.5px;line-height:26px;opacity:.9}
.service{position:absolute;top:236px;width:200px;text-align:center;font-size:14px;font-weight:500}
.service svg{display:block;margin:0 auto 18px;width:60px;height:60px}

/* work */
.work{left:0;top:1827px;width:1200px;height:559px;background:var(--light)}
.card{top:1928px;width:267px;height:356px;background:var(--white)}
.card .photo{width:100%;height:187px}
.card h3{position:absolute;left:36px;top:226px;font-size:22px;font-weight:500;color:var(--ink)}
.card small{position:absolute;left:36px;top:258px;font-size:9px;letter-spacing:.5px;color:var(--faint);text-transform:uppercase}
.card .price{position:absolute;left:36px;top:284px;font-size:20px;font-weight:600;color:var(--ink)}
.card.raised{box-shadow:0 18px 40px rgba(0,0,0,.12)}
.work-heading{left:839px;top:2028px;font-size:27px;line-height:37px;font-weight:400}
.ctrl{top:2162px;width:44px;height:44px;border-radius:50%;background:var(--white);display:flex;align-items:center;justify-content:center}

/* testimonials */
.section-heading{left:0;width:1200px;text-align:center;font-size:27px;font-weight:400}
.avatar{width:62px;height:62px;border-radius:50%;background:linear-gradient(160deg,#e9d8c8,#b79a84)}
.t-name{font-size:14px;font-weight:500;color:var(--ink)}
.t-title{font-size:20px;font-weight:400;color:var(--ink)}
.dot{width:7px;height:7px;border-radius:50%;background:#cfd3da}

/* newsletter */
.newsletter{left:0;top:2846px;width:1200px;height:137px;background:var(--accent)}
.newsletter h2{position:absolute;left:88px;top:54px;font-size:21px;font-weight:500;color:var(--white)}
.news-input{position:absolute;left:755px;top:45px;width:366px;height:47px;background:var(--white);display:flex;align-items:center;padding:0 18px;gap:12px;font-size:12px;color:var(--faint)}

/* footer */
.footer{left:0;top:2983px;width:1200px;height:345px;background:var(--footer);color:#d6dbe3}
.f-col{position:absolute;top:78px}
.f-col h4{font-size:14px;font-weight:500;color:var(--white);margin-bottom:14px}
.f-col li{list-style:none;font-size:12px;line-height:36px;color:#c3c9d3;display:flex;align-items:center;gap:10px}
.f-col li i{display:block;width:8px;height:8px;border-radius:50%;background:#c3c9d3}
.f-contact{font-size:12px;line-height:24px;color:#c3c9d3}
.f-contact b{color:var(--white);font-weight:500}
.bottom-bar{left:0;top:3328px;width:1200px;height:55px;background:var(--footer-deep);text-align:center;font-size:12px;line-height:55px;color:#c3c9d3}
.to-top{left:1133px;top:3306px;width:45px;height:45px;border-radius:50%;background:var(--white);display:flex;align-items:center;justify-content:center;box-shadow:0 2px 8px rgba(0,0,0,.2)}
</style>
</head>
<body>

<header class="abs site-header">
  <div class="abs brand">VELTA CORE</div>
  <nav class="abs nav">
    <span class="active">Home</span><span>About us</span><span>Services ▾</span><span>Our Work</span><span>Our Partners</span><span>Contact us</span>
  </nav>
</header>

<section>
  <div class="abs hero" role="img" aria-label="Bright marble bathroom with white basins and chrome taps"></div>
  <div class="abs hero-shade"></div>
  <div class="abs hero-kicker">We do all domestic &amp; commercial</div>
  <h1 class="abs hero-title serif">Wall and floor tiling</h1>
  <div class="abs hero-btn">GET IN TOUCH WITH US</div>
  <svg class="abs hero-arrow" style="left:21px" viewBox="0 0 44 44"><path d="M25 15l-7 7 7 7" fill="none" stroke="#fff" stroke-width="2"/></svg>
  <svg class="abs hero-arrow" style="left:1135px" viewBox="0 0 44 44"><path d="M19 15l7 7-7 7" fill="none" stroke="#fff" stroke-width="2"/></svg>
</section>

<section>
  <div class="abs partner" style="left:112px"><i></i>Ardent Studio</div>
  <div class="abs partner" style="left:318px"><i></i>BRAVEN costruction</div>
  <div class="abs partner" style="left:555px"><i></i>lumo properties</div>
  <div class="abs partner" style="left:775px"><i></i>Tilvor</div>
  <div class="abs partner" style="left:985px"><i></i>TWD</div>
</section>

<section>
  <div class="abs eyebrow" style="left:88px;top:909px">About us</div>
  <h2 class="abs about-heading serif">Short Introduction<br>about our work.</h2>
  <p class="abs body-text" style="left:88px;top:1028px;width:330px">Etiam ultricies nisi vel augue curabitur ullam corper ultricies nisi nam eget dui etiam rhoncus maecenas tempus ipsum.</p>
  <p class="abs body-text" style="left:88px;top:1108px;width:330px">Curabitur ullam corper ultricies nisi nam eget dui etiam rhoncus maecenas tempus lorem.</p>
  <div class="abs btn-accent" style="left:88px;top:1195px;width:138px;height:43px">LEARN MORE</div>
  <div class="abs about-photo" role="img" aria-label="Bathroom with glass shower, marble walls and granite vanity"></div>
</section>

<section class="abs services">
  <h2>We do tilings and much more</h2>
  <p>Etiam ultricies nisi vel augue curabitur ullam corper ultricies nisi nam eget dui etiam rhoncus maecenas tempus ipsum.</p>
  <div class="service" style="left:119px">
    <svg viewBox="0 0 60 60" fill="none" stroke="#fff" stroke-width="2"><path d="M18 40V12a6 6 0 0 1 12 0M34 40V12a6 6 0 0 1 12 0M18 20h16M18 30h16"/><path d="M6 46c6 4 10 4 16 0s10-4 16 0 10 4 16 0M6 54c6 4 10 4 16 0s10-4 16 0 10 4 16 0"/></svg>
    Swimming Pool</div>
  <div class="service" style="left:371px">
    <svg viewBox="0 0 60 60" fill="none" stroke="#fff" stroke-width="2"><rect x="8" y="20" width="44" height="8" rx="3"/><path d="M14 28v22M46 28v22M14 40h32M20 20c0-6 6-8 10-8"/></svg>
    Spas</div>
  <div class="service" style="left:626px">
    <svg viewBox="0 0 60 60" fill="none" stroke="#fff" stroke-width="2"><rect x="8" y="8" width="44" height="44"/><path d="M8 19h44M8 30h44M8 41h44M22 8v11M38 8v11M16 19v11M30 19v11M44 19v11M22 30v11M38 30v11M16 41v11M30 41v11M44 41v11"/></svg>
    Paving</div>
  <div class="service" style="left:910px">
    <svg viewBox="0 0 60 60" fill="none" stroke="#fff" stroke-width="2"><ellipse cx="30" cy="46" rx="24" ry="8"/><ellipse cx="30" cy="32" rx="18" ry="7"/><ellipse cx="30" cy="18" rx="12" ry="7"/></svg>
    Marbles blue stones</div>
</section>

<section>
  <div class="abs work"></div>
  <article class="abs card" style="left:-53px">
    <div class="photo" role="img" aria-label="Outdoor rooftop pool at sunset overlooking city towers" style="background:linear-gradient(180deg,#8fa7c9 0%,#e7b38c 60%,#4b5d78 100%)"></div>
    <h3>Outdoor Tiling</h3><small>Outdoor tiling starting from</small><div class="price">$50.99</div>
  </article>
  <article class="abs card" style="left:216px">
    <div class="photo" role="img" aria-label="Tiled bathroom with arched mirror and vanity" style="background:linear-gradient(160deg,#cdbfae 0%,#a4907c 55%,#6e6257 100%)"></div>
    <h3>Indoor Tiling</h3><small>Indoor tiling starting from</small><div class="price">$50.99</div>
  </article>
  <article class="abs card raised" style="left:484px">
    <div class="photo" role="img" aria-label="Grey and white rectangular paving tiles" style="background:linear-gradient(135deg,#9a9ca0 0%,#d6d7d9 50%,#7e8084 100%)"></div>
    <h3>Paving</h3><small>Paving starting from</small><div class="price">$50.99</div>
  </article>
  <svg class="abs" style="left:686px;top:2264px" width="42" height="42" viewBox="0 0 42 42"><circle cx="21" cy="21" r="18" fill="#fff" stroke="var(--accent)" stroke-width="3"/><path d="M21 13v16M15 19l6-6 6 6" fill="none" stroke="var(--ink)" stroke-width="2"/></svg>
  <div class="abs eyebrow" style="left:839px;top:2007px">Our work</div>
  <h2 class="abs work-heading serif">Our Indoor/Outdoor<br>Tiling work.</h2>
  <div class="abs ctrl" style="left:837px;border:1px solid #d4d7dd"><svg width="14" height="14" viewBox="0 0 14 14"><path d="M9 2L4 7l5 5" fill="none" stroke="#888" stroke-width="1.6"/></svg></div>
  <div class="abs ctrl" style="left:891px;border:2px solid var(--accent)"><svg width="14" height="14" viewBox="0 0 14 14"><path d="M5 2l5 5-5 5" fill="none" stroke="var(--accent)" stroke-width="1.6"/></svg></div>
</section>

<section>
  <div class="abs eyebrow" style="left:0;width:1200px;text-align:center;top:2492px">Happy customers</div>
  <h2 class="abs section-heading serif" style="top:2514px">See what our customers saay</h2>

  <div class="abs avatar" style="left:88px;top:2588px" role="img" aria-label="Customer portrait"></div>
  <div class="abs t-name" style="left:180px;top:2597px">Mara Quill.</div>
  <div class="abs t-title serif" style="left:180px;top:2622px">Simply Awesome lighting Products</div>
  <p class="abs body-text" style="left:180px;top:2662px;width:370px">"Maecenas tempus tellus eget condimentum rhoncus sem quam semper libero, sit amet adipiscing sem neque sed ipsum nam quam nunc"</p>

  <div class="abs avatar" style="left:660px;top:2588px" role="img" aria-label="Customer portrait"></div>
  <div class="abs t-name" style="left:751px;top:2597px">Ellis Drummond.</div>
  <div class="abs t-title serif" style="left:751px;top:2622px">Great! Simple and Smart lighting</div>
  <p class="abs body-text" style="left:751px;top:2662px;width:370px">"Lorem ipsum dolor tempus tellus eget condimentum rhoncus sem quam semper libero, sit amet adipiscing sem neque sed ipsum nam quam"</p>

  <div class="abs dot" style="left:1151px;top:2650px;background:#4cc87a"></div>
  <div class="abs dot" style="left:1151px;top:2664px"></div>
  <div class="abs dot" style="left:1151px;top:2678px"></div>
</section>

<section class="abs newsletter">
  <h2>Subscribe to our email newsletter</h2>
  <div class="news-input">
    <svg width="14" height="10" viewBox="0 0 14 10"><rect x=".5" y=".5" width="13" height="9" fill="none" stroke="#aab" /><path d="M.5 .5l6.5 5 6.5-5" fill="none" stroke="#aab"/></svg>
    <span style="flex:1">Enter your email address</span>
    <svg width="16" height="16" viewBox="0 0 16 16"><path d="M1 8l14-7-5 14-2-6z" fill="#222"/></svg>
  </div>
</section>

<footer class="abs footer">
  <div class="f-col" style="left:88px"><h4>Quick links</h4><ul><li>Home</li><li>About</li><li>Privacy Policy</li><li>Terms &amp; Conditions</li><li>Contact us</li></ul></div>
  <div class="f-col" style="left:343px"><h4>Services</h4><ul><li>Tiling</li><li>Spas</li><li>Paving</li><li>Marbles blue stones</li></ul></div>
  <div class="f-col" style="left:604px"><h4>Keep in touch</h4>
    <div class="f-contact" style="position:relative;padding-left:18px;margin-top:6px">
      <svg style="position:absolute;left:0;top:6px" width="10" height="13" viewBox="0 0 10 13"><path d="M5 0a5 5 0 0 1 5 5c0 4-5 8-5 8S0 9 0 5a5 5 0 0 1 5-5z" fill="var(--accent)"/><circle cx="5" cy="5" r="2" fill="var(--footer)"/></svg>
      <b>Address:</b><br>Some address line goes here,<br>City name, Country name.
    </div>
    <div class="f-contact" style="position:relative;padding-left:18px;margin-top:22px">
      <svg style="position:absolute;left:0;top:8px" width="11" height="8" viewBox="0 0 11 8"><rect width="11" height="8" fill="var(--accent)"/></svg>
      <b>Email address:</b><br>info@veltacore.com
    </div>
  </div>
  <div class="f-col" style="left:898px"><h4>Follow us</h4><ul><li><i></i>Friendnet</li><li><i></i>Chirper</li><li><i></i>Circles</li><li><i></i>Worklink</li><li><i></i>Viewtube</li></ul></div>
</footer>
<div class="abs bottom-bar">© 2017, All Rights Reserved</div>
<div class="abs to-top"><svg width="14" height="14" viewBox="0 0 14 14"><path d="M7 12V2M3 6l4-4 4 4" fill="none" stroke="#333" stroke-width="1.6"/></svg></div>

</body>
</html>
```